Sphynx Cat Breeder

Hi.
I have just got a logo through Pixel Harbor, and now I need a website.
I am home based Sphynx cat breeder (Plumwick Sphynx)
I want to be able to show my breedings cats and kittens available for sale on my website.

Target Market(s)

Buyers of pet kittens in New Zealand, plus potentially buyers of kittens for breeding for overseas breeders

Requirements
Must have
• Home page
About Us
My breeding Cats
Kittens
Caring for a Sphynx
Links
Contact (contact details plus a link to email)
I need to be able to upload photos as kittens come and go.
Nice to have
• A web counter, visible only to me, preferably showing which country they are from

```html
<!DOCTYPE html>
<html lang="en">
<head>
<meta charset="utf-8">
<title>Plumwick Sphynx</title>
<link href="https://fonts.googleapis.com/css2?family=Open+Sans:wght@400;600;700&display=swap" rel="stylesheet">
<style>
:root{
  --page-top:#f4f5f7;
  --page-bottom:#dfe4ea;
  --panel:#ffffff;
  --panel-edge:#c9cdd2;
  --ink:#2b2b2b;
  --body-text:#3a3a3a;
  --link-text:#444444;
  --btn-grey-top:#b9b9b9;
  --btn-grey-bottom:#7d7d7d;
  --btn-blue-top:#6cc6ef;
  --btn-blue-bottom:#3ba3d8;
  --btn-border:#2f2f2f;
  --accent:#59b6e2;
  --rule:#9a9a9a;
  --logo:#1e1e1e;
}
*{margin:0;padding:0;box-sizing:border-box}
html,body{width:1200px;height:900px;overflow:hidden}
body{
  font-family:"Open Sans",Arial,sans-serif;
  color:var(--ink);
  background:
    repeating-linear-gradient(0deg,rgba(255,255,255,.35) 0 1px,transparent 1px 3px),
    linear-gradient(180deg,var(--page-top),var(--page-bottom));
  position:relative;
}
.site-panel{
  position:absolute;left:165px;top:69px;width:870px;height:860px;
  background:var(--panel);border:1px solid var(--panel-edge);border-radius:3px;
  box-shadow:0 0 6px rgba(0,0,0,.08);
}
.logo-tab{position:absolute;left:503px;top:19px;width:180px;height:52px}
.brand{position:absolute;text-align:center;color:var(--logo)}
.brand-circle{border:9px solid var(--logo);border-radius:50%;margin:0 auto}
.brand-name{font-weight:700;white-space:nowrap}
.brand-header{left:520px;top:38px;width:160px}
.brand-header .brand-circle{width:96px;height:96px}
.brand-header .brand-name{font-size:14px;margin-top:6px}
.brand-footer{left:860px;top:787px;width:125px}
.brand-footer .brand-circle{width:62px;height:62px;border-width:6px}
.brand-footer .brand-name{font-size:10px;margin-top:5px}

.nav-btn{
  position:absolute;top:110px;height:31px;
  border:1px solid var(--btn-border);border-radius:4px;
  background:linear-gradient(180deg,var(--btn-grey-top),var(--btn-grey-bottom));
  color:#fff;font-size:13px;font-weight:700;
  display:flex;align-items:center;justify-content:center;
  text-shadow:0 1px 1px rgba(0,0,0,.45);
  box-shadow:inset 0 1px 0 rgba(255,255,255,.5),0 1px 2px rgba(0,0,0,.25);
}
.nav-btn.is-active{background:linear-gradient(180deg,var(--btn-blue-top),var(--btn-blue-bottom))}

.hero-frame{
  position:absolute;left:181px;top:214px;width:838px;height:269px;
  border:1px solid #e2c9c6;border-radius:3px;background:#fdf8f7;
}
.hero-shadow{
  position:absolute;left:230px;top:480px;width:740px;height:12px;border-radius:50%;
  box-shadow:0 6px 8px -4px rgba(0,0,0,.55);
}
.hero-photo{
  position:absolute;left:189px;top:222px;width:822px;height:252px;
  background:
    radial-gradient(ellipse at 48% 55%,#e8b68f 0%,#c98a5e 35%,transparent 70%),
    linear-gradient(90deg,#5a3a28,#b97a50 30%,#d9a27a 60%,#c48c68 85%,#7a5540);
}
.hero-caption{
  position:absolute;left:189px;top:432px;width:822px;height:42px;
  background:rgba(15,15,15,.78);color:#fff;font-size:13px;
  padding-left:19px;line-height:42px;
}

.section-title{position:absolute;top:515px;font-size:15px;font-weight:600;display:flex;align-items:center;gap:12px}
.section-title .mark{width:7px;height:7px;background:var(--ink);border-radius:50%}
.about-title{left:182px}
.kittens-title{left:468px}
.about-text{
  position:absolute;left:182px;top:554px;width:266px;
  font-size:11px;line-height:17.8px;color:var(--body-text);
}
.read-more{
  position:absolute;left:183px;top:679px;width:123px;height:48px;
  background:var(--accent);border-radius:3px;color:#fff;
  font-size:14px;font-weight:600;display:flex;align-items:center;justify-content:center;
}
.kitten-grid{
  position:absolute;left:469px;top:558px;
  display:grid;grid-template-columns:repeat(6,79px);column-gap:15px;row-gap:8px;
}
.kitten-thumb{width:79px;height:63px}
.kitten-thumb.tabby{background:linear-gradient(135deg,#cfcfcf,#8a8a8a 55%,#4d4d4d)}
.kitten-thumb.ginger{background:linear-gradient(135deg,#e49a55,#c9744a 50%,#7d6d8c)}

.footer-col{position:absolute;top:784px;width:197px}
.footer-col h3{
  font-size:14px;font-weight:600;text-align:center;
  padding-bottom:6px;border-bottom:1px solid var(--rule);margin-bottom:5px;
}
.link-list{display:grid;grid-template-columns:86px 100px;font-size:11px;line-height:18px;color:var(--link-text);list-style:none}
.site-links{left:181px}
.other-links{left:394px}
.contact-col{left:608px}
.contact-list{list-style:none;font-size:11px;color:var(--ink)}
.contact-list li{display:flex;align-items:center;height:25px}
.contact-list svg{width:14px;height:14px;margin-right:11px;flex:none}
.contact-list b{font-weight:700;margin-right:3px}
</style>
</head>
<body>
<svg class="logo-tab" viewBox="0 0 180 52" aria-hidden="true">
  <path d="M2 51 C14 51 10 34 30 30 C48 26 60 22 72 8 Q90 -4 108 8 C120 22 132 26 150 30 C170 34 166 51 178 51" fill="#fff" stroke="#c9cdd2"/>
</svg>
<div class="site-panel"></div>
<svg class="logo-tab" viewBox="0 0 180 52" aria-hidden="true" style="top:21px">
  <path d="M4 52 C16 52 12 36 31 32 C49 28 61 24 73 10 Q90 -2 107 10 C119 24 131 28 149 32 C168 36 164 52 176 52Z" fill="#fff"/>
</svg>

<div class="brand brand-header"><div class="brand-circle"></div><div class="brand-name">Plumwick Sphynx</div></div>

<nav>
  <div class="nav-btn is-active" style="left:182px;width:71px">Home</div>
  <div class="nav-btn" style="left:269px;width:90px">About Us</div>
  <div class="nav-btn" style="left:374px;width:143px">My Breeding Cats</div>
  <div class="nav-btn" style="left:688px;width:80px">Kittens</div>
  <div class="nav-btn" style="left:785px;width:134px">Caring a Spyhnx</div>
  <div class="nav-btn" style="left:935px;width:83px">Contact</div>
</nav>

<div class="hero-shadow"></div>
<div class="hero-frame"></div>
<div class="hero-photo" role="img" aria-label="Close-up photo of a ginger kitten"></div>
<div class="hero-caption">Cute Brown Kittens</div>

<h2 class="section-title about-title"><span class="mark"></span>About Us</h2>
<p class="about-text">Lorem ipsum dolor sit amet, consectetur adipisicing elit, sed do eiusmod tempor incididunt ut labore et dolore magna aliqua. Ut enim ad minim veniam, quis nostrud exercitation ullamco.Ut enim ad minim veniam, quis nostrud exercitation ullamco.Ut enim ad minim veniam, quis nostrud exercitation ullamco.</p>
<div class="read-more">Read More</div>

<h2 class="section-title kittens-title"><span class="mark"></span>Newest Kittens</h2>
<div class="kitten-grid">
  <div class="kitten-thumb tabby" role="img" aria-label="Photo of a grey tabby kitten"></div>
  <div class="kitten-thumb ginger" role="img" aria-label="Photo of a ginger kitten"></div>
  <div class="kitten-thumb tabby" role="img" aria-label="Photo of a grey tabby kitten"></div>
  <div class="kitten-thumb ginger" role="img" aria-label="Photo of a ginger kitten"></div>
  <div class="kitten-thumb tabby" role="img" aria-label="Photo of a grey tabby kitten"></div>
  <div class="kitten-thumb ginger" role="img" aria-label="Photo of a ginger kitten"></div>
  <div class="kitten-thumb tabby" role="img" aria-label="Photo of a grey tabby kitten"></div>
  <div class="kitten-thumb ginger" role="img" aria-label="Photo of a ginger kitten"></div>
  <div class="kitten-thumb tabby" role="img" aria-label="Photo of a grey tabby kitten"></div>
  <div class="kitten-thumb ginger" role="img" aria-label="Photo of a ginger kitten"></div>
  <div class="kitten-thumb tabby" role="img" aria-label="Photo of a grey tabby kitten"></div>
  <div class="kitten-thumb ginger" role="img" aria-label="Photo of a ginger kitten"></div>
</div>

<footer>
  <div class="footer-col site-links">
    <h3>Site Links</h3>
    <ul class="link-list"><li>Your Link</li><li>Your Link</li><li>Other Link</li><li>Other Link</li><li>Third Link</li><li>Third Link</li></ul>
  </div>
  <div class="footer-col other-links">
    <h3>Other Links</h3>
    <ul class="link-list"><li>Your Link</li><li>Your Link</li><li>Other Link</li><li>Other Link</li><li>Third Link</li><li>Third Link</li></ul>
  </div>
  <div class="footer-col contact-col">
    <h3>Contact Details</h3>
    <ul class="contact-list">
      <li><svg viewBox="0 0 14 14"><path d="M7 1a4 4 0 0 0-4 4c0 3 4 8 4 8s4-5 4-8a4 4 0 0 0-4-4zm0 5.5a1.5 1.5 0 1 1 0-3 1.5 1.5 0 0 1 0 3z" fill="#2b2b2b"/></svg><b>P.O.BOX :</b> 4172, Nelson , NZ</li>
      <li><svg viewBox="0 0 14 14"><path d="M3 1l2.5 3-1.3 1.5c.8 1.8 2.3 3.3 4.3 4.3L10 8.5l3 2.5-1.5 2C6 12.5 1.5 8 1 2.5z" fill="#2b2b2b"/></svg><b>Telephone :</b> 0064 3 555 0172</li>
      <li><svg viewBox="0 0 14 14"><rect x="1" y="3" width="12" height="8" fill="#2b2b2b"/><path d="M1.5 3.5L7 8l5.5-4.5" stroke="#fff" fill="none"/></svg><b>Email :</b> hello@plumwick.example</li>
    </ul>
  </div>
</footer>

<div class="brand brand-footer"><div class="brand-circle"></div><div class="brand-name">Plumwick Sphynx</div></div>
</body>
</html>
```